Simple Modern Label for a Coconut oil product

We need a label designed for Organic Coconut oil. We would like the label to convey the gourmet/high quality product. It should be modern and simple and look like an artisinal product. The label will need to contain all the basic label requirements - Independence list, place for nutrition facts, our company logo etc.
The label will ultimately be printed as oil proof, so it will have a glossy appearance.
I have includes some examples that I like and a file with the logo.

Product Container - Wide Mount Clear Glass Jar: 4.75 inches tall (base to the bottom of the lid) and 9.5 in circumference
Label: Can be 1 or 2 separate labels, round, square and rectangle are okay
No larger than 3 inches high and 9 inches long

Target Market(s)

Middle Age home chef

Industry/Entity Type

Product

Requirements
Must have
• - logo (Attached below, I have this in multiple formats, let me know if you need them)
• - 14 FL OZ (414mL)
• - ingredient: organic unrefined whole kernel virgin coconut oil,
• - Manufacturer: XXX Y St., anywhere, CA, 99999
• - Distributed by Meadowfern Naturals, P.O. Box 5521, Oakland, CA 94612 www.MeadowfernNaturals.example
• - Certified Organic by Company Name
• - Product of Sri Lanka
Nice to have
• - Nutrition Facts
Should not have
• Clutter

```html
<!DOCTYPE html>
<html lang="en">
<head>
<meta charset="utf-8">
<title>Meadowfern Naturals – Organic Virgin Coconut Oil Labels</title>
<link href="https://fonts.googleapis.com/css2?family=Montserrat:wght@700&family=Poiret+One&display=swap" rel="stylesheet">
<style>
  :root{
    --bg:#e6e6e6;
    --black-a:#141414;
    --black-b:#3a3a3a;
    --teal-a:#7fc6b4;
    --teal-b:#b3ebe2;
    --navy:#1e2a5a;
    --white:#ffffff;
    --silver:#c9c9c9;
    --lid-white:#f7f7f7;
  }
  *{margin:0;padding:0;box-sizing:border-box}
  html,body{width:1200px;height:1200px;overflow:hidden;background:var(--bg)}
  .sheet{position:relative;width:1200px;height:1200px}
  .lid{position:absolute;top:90px;width:320px;height:320px;border-radius:50%;
       display:flex;flex-direction:column;align-items:center;justify-content:center;gap:18px}
  .lid--dark{left:110px;background:var(--silver);border:14px solid var(--black-a);color:var(--black-a)}
  .lid--light{left:770px;background:var(--lid-white);border:14px solid #fff;box-shadow:0 0 0 2px #d8d8d8;color:var(--navy)}
  .lid .mark{width:70px;height:70px;border-radius:50%;background:currentColor;opacity:.85}
  .brand{font-family:"Montserrat",sans-serif;font-weight:700;letter-spacing:1px;text-align:center;line-height:1}
  .lid .brand{font-size:26px}
  .label{position:absolute;top:480px;width:440px;height:560px;
         display:flex;flex-direction:column;align-items:center;padding-top:90px}
  .label--dark{left:50px;background:linear-gradient(90deg,var(--black-a),var(--black-b) 60%,var(--black-a));color:var(--white)}
  .label--teal{left:710px;background:linear-gradient(100deg,var(--teal-a),var(--teal-b));color:var(--navy)}
  .label .mark{width:150px;height:150px;border-radius:50%}
  .label--dark .mark{background:var(--silver)}
  .label--teal .mark{background:#d6f1ec;border:6px solid var(--navy)}
  .label .brand{font-size:34px;margin-top:40px}
  .rule{width:340px;height:2px;background:currentColor;margin:14px 0 16px;opacity:.8}
  .product{font-family:"Poiret One",sans-serif;font-size:40px;line-height:1;text-align:center}
  .volume{font-family:"Montserrat",sans-serif;font-weight:700;font-size:16px;letter-spacing:3px;margin-top:28px}
</style>
</head>
<body>
<main class="sheet">
  <section class="lid lid--dark">
    <span class="mark"></span>
    <p class="brand">MEADOWFERN<br>NATURALS</p>
  </section>
  <section class="lid lid--light">
    <span class="mark"></span>
    <p class="brand">MEADOWFERN<br>NATURALS</p>
  </section>

  <section class="label label--dark">
    <span class="mark"></span>
    <p class="brand">MEADOWFERN NATURALS</p>
    <div class="rule"></div>
    <p class="product">organic virgin<br>coconut oil</p>
    <p class="volume">14 FL . OZ</p>
  </section>
  <section class="label label--teal">
    <span class="mark"></span>
    <p class="brand">MEADOWFERN NATURALS</p>
    <div class="rule"></div>
    <p class="product">organic virgin<br>coconut oil</p>
    <p class="volume">14 FL . OZ</p>
  </section>
</main>
</body>
</html>
```